Label or packaging Design for Hair Care Line

Dear Designer,
We are Corvella, a brand known for our premium hairstyling tools, and we are excited to expand into hair care. We are currently looking for a talented designer to create the label designs for our entire luxury hair care line.
This project is crucial in establishing our visual identity in the hair care market, and we aim to position ourselves alongside premium brands such as PLX, Varnette Coif Atelier, and Trevo.
Project Scope
We need a cohesive label design for our hair care line, which includes:
5 products (e.g., shampoo, conditioner, hair oil, styling cream, and a hair mask).
The designs should include:
Front label: Highlighting the product name, key features, and branding.
Our goal is to achieve a design that communicates premium luxury with a touch of professionalism. Below are the specific guidelines to help you align with our vision:
Style and Inspiration
Think of brands like PLX, Varnette Coif Atelier, and Trevo.
Luxury and Minimalism: Clean lines, sophisticated typography, and an elegant color palette.
Subtle femininity: premium finishes like metallic accents (gold, silver, or rose gold).
Brand Personality
Premium: Reflecting high quality and exclusivity.
Modern & Professional: Appealing to a refined, professional audience but also suitable for lifestyle-oriented customers.
Warm & Empowering: A brand that celebrates confidence and individuality.
Color Palette
Neutral tones like black, white, accented with metallics (gold or silver) for a luxurious feel.
Colors that feel timeless and elegant rather than trendy or overly bright.
Typography
Use clean, modern fonts (preferably sans-serif or serif for a refined look).
Clear and legible for all product details while maintaining a high-end aesthetic.
Materials and Finishes
Packaging Shape
The label designs should suit a variety of bottle and jar shapes (e.g., cylindrical, flat, or rounded).
Keep scalability in mind so the identity remains consistent across different products.
Deliverables
To understand the aesthetic we are aiming for, here are some brands to use as inspiration:
PLX: For its minimalistic and modern approach.
Varnette Coif Atelier: For its combination of luxury and professional appeal.
Trevo: For its soft femininity and lifestyle branding.
we would like to see your designs applied to a variety of packaging types to get an overall impression of how the brand identity works across different product formats. This includes:
A squeeze bottle (e.g., for styling creams or conditioners).
A glass bottle with a dropper (e.g., for a luxurious hair oil).
A shampoo/conditioner bottle (standard pump or flip-top cap).
A spray bottle (e.g., for leave-in treatments or heat protectors).
By creating designs for these different packaging types, we can better evaluate how cohesive and versatile the brand identity will be across the entire product line.

Updates
As you may have noticed from the designs, they don’t quite align with our briefing. The look needs to be clean and professional, similar to Varnette, PLX, and the other examples we provided. Please address this, and we’ll check it!

Target Market(s)
europe and us
Font styles to use
Other font styles liked:
- century gothic

Look and feel
Each slider illustrates characteristics of the customer's brand and the style your logo design should communicate.

```html
<!DOCTYPE html>
<html lang="en">
<head>
<meta charset="UTF-8">
<title>Corvella Hair Care Labels</title>
<link href="https://fonts.googleapis.com/css2?family=Mulish:wght@300;400;600&display=swap" rel="stylesheet">
<style>
  :root {
    --backdrop: #3b3b3c;
    --label-black: #141414;
    --gold: #d9ad62;
    --gold-light: #e8c888;
    --gold-deep: #c8924a;
    --text-soft: #c9c9c9;
    --text-dim: #9a9a9a;
  }
  * { margin: 0; padding: 0; box-sizing: border-box; }
  html, body {
    width: 1200px; height: 800px; overflow: hidden;
    background: var(--backdrop);
    font-family: "Mulish", sans-serif;
  }
  .label-line {
    position: relative;
    width: 1200px; height: 800px;
    display: flex; align-items: center; justify-content: center; gap: 70px;
  }
  .label {
    position: relative;
    background: var(--label-black);
    border-radius: 6px;
    box-shadow: 0 10px 30px rgba(0,0,0,0.35);
  }
  .label--spray   { width: 280px; height: 460px; }
  .label--shampoo { width: 280px; height: 460px; }
  .label--oil     { width: 200px; height: 320px; }

  .brand-mark-area {
    position: absolute;
    left: 24px; top: 48px;
    width: 190px; height: 190px;
    border-radius: 4px;
    background: linear-gradient(135deg, rgba(232,200,136,0.28), rgba(200,146,74,0.12));
  }
  .label--oil .brand-mark-area {
    left: 16px; top: 30px;
    width: 130px; height: 130px;
  }

  .brand-name {
    position: absolute;
    right: 22px; bottom: 30px;
    writing-mode: vertical-rl;
    transform: rotate(180deg);
    color: var(--gold);
    font-weight: 300;
    font-size: 46px;
    letter-spacing: 1px;
    line-height: 1;
  }
  .label--oil .brand-name { font-size: 30px; right: 16px; bottom: 22px; }

  .product-info {
    position: absolute;
    left: 24px; bottom: 92px;
    color: var(--text-soft);
    font-size: 12px;
    line-height: 1.3;
    font-weight: 400;
  }
  .product-name {
    display: block;
    margin-top: 3px;
    color: var(--gold-deep);
    font-weight: 600;
    font-size: 12px;
    letter-spacing: 2px;
    text-transform: uppercase;
  }
  .volume {
    position: absolute;
    left: 24px; bottom: 44px;
    color: var(--text-dim);
    font-size: 11px;
  }
  .label--oil .product-info { left: 16px; bottom: 70px; font-size: 9px; }
  .label--oil .product-name { font-size: 14px; font-weight: 400; color: var(--gold); letter-spacing: 2px; }
  .label--oil .volume { left: 16px; bottom: 48px; font-size: 7px; }
</style>
</head>
<body>
  <main class="label-line">
    <section class="label label--spray">
      <div class="brand-mark-area" role="img" aria-label="Gold brand monogram area"></div>
      <p class="product-info">honey infused<br>leave-in conditioner<span class="product-name">Healthy Hair</span></p>
      <p class="volume">150ml -5.1fl.oz.</p>
      <span class="brand-name">corvella</span>
    </section>

    <section class="label label--shampoo">
      <div class="brand-mark-area" role="img" aria-label="Gold brand monogram area"></div>
      <p class="product-info">honey infused<br>leave-in conditioner<span class="product-name">Shampoo</span></p>
      <p class="volume">150ml -5.1fl.oz.</p>
      <span class="brand-name">corvella</span>
    </section>

    <section class="label label--oil">
      <div class="brand-mark-area" role="img" aria-label="Gold brand monogram area"></div>
      <p class="product-info">honey infused<br>leave-in conditioner<span class="product-name">Hair Oil</span></p>
      <p class="volume">150ml -5.1fl.oz.</p>
      <span class="brand-name">corvella</span>
    </section>
  </main>
</body>
</html>
```